Flyer design - company flyer

We would like to inform about and advertise our services. There fore we would like to create a flyer with that information. We'll need a design to ge it done. We are looking for a design aligned with our website and logo. CAUTION - new website. current brenvaro.de is old! You can find our new website which should be represented at: beta.brenvaro.de

```html
<!DOCTYPE html>
<html lang="en">
<head>
<meta charset="utf-8">
<title>Brenvaro – Company Flyer</title>
<link href="https://fonts.googleapis.com/css2?family=Montserrat:wght@500;600;700;800;900&family=Open+Sans:wght@400;600;700&display=swap" rel="stylesheet">
<style>
:root{
  --blue:#1f6fc5;
  --blue-dark:#1558a3;
  --ink:#222831;
  --muted:#5b6270;
  --panel:#ececec;
  --stage:#d6d6d6;
  --white:#ffffff;
  --line:#c9ced6;
}
*{box-sizing:border-box;margin:0;padding:0}
html,body{width:900px;height:1200px;overflow:hidden}
body{background:var(--stage);font-family:"Open Sans",Arial,sans-serif;color:var(--ink);position:relative}
.page{position:absolute;top:303px;width:420px;height:594px;background:var(--white);overflow:hidden;box-shadow:0 2px 8px rgba(0,0,0,.15)}
.page--front{left:20px}
.page--back{left:460px}
.abs{position:absolute}
.heading{font-family:"Montserrat",Arial,sans-serif;font-weight:700;letter-spacing:.5px;color:var(--ink)}

/* front */
.brand{left:28px;top:28px;display:flex;align-items:center;gap:6px}
.brand__mark{width:11px;height:11px;background:var(--blue)}
.brand__name{font-family:"Montserrat",sans-serif;font-weight:700;font-size:17px;letter-spacing:2px;color:var(--blue)}
.hero-photo{left:170px;top:48px;width:250px;height:210px;background:linear-gradient(135deg,#f4f5f7 0%,#dfe3e8 45%,#c7a48a 70%,#d36a3e 100%)}
.hero-title{left:28px;top:78px;font-family:"Montserrat",sans-serif;font-weight:800;font-size:50px;line-height:.98;color:var(--blue);letter-spacing:-1px}
.hero-sub{left:30px;top:198px;font-family:"Montserrat",sans-serif;font-weight:600;font-size:8px;line-height:1.3;color:var(--ink)}
.band{left:0;top:225px;width:420px;height:60px}
.about{left:0;top:258px;width:172px;height:300px;background:var(--panel);padding:30px 14px 0 30px}
.about .heading{font-size:12px}
.about__rule{width:26px;height:1px;background:var(--muted);margin:4px 0 10px}
.about__label{font-family:"Montserrat",sans-serif;font-size:6px;font-weight:700;color:var(--blue);margin-bottom:4px}
.about p{font-size:5.5px;line-height:1.45;color:var(--muted);text-align:justify}
.founder{display:flex;gap:8px;margin-top:12px}
.founder__photo{flex:0 0 40px;height:58px;background:linear-gradient(180deg,#c9c6c2,#8c8884)}
.founder__name{font-family:"Montserrat",sans-serif;font-size:7px;font-weight:600;color:var(--blue)}
.founder__role{font-size:5.5px;color:var(--muted);margin-bottom:4px}
.benefits{left:200px;top:285px;width:200px}
.benefits .heading{font-size:12px}
.benefits__rule{width:26px;height:1px;background:var(--muted);margin:4px 0 14px}
.benefit-grid{display:grid;grid-template-columns:1fr 1fr;column-gap:12px;row-gap:12px}
.benefit{position:relative;padding-bottom:8px;border-bottom:1px dashed var(--line)}
.benefit__head{display:flex;gap:6px;align-items:center;margin-bottom:5px}
.benefit__head svg{width:14px;height:14px;flex:0 0 14px}
.benefit__title{font-family:"Montserrat",sans-serif;font-size:6.5px;line-height:1.15;color:var(--blue);font-weight:500}
.benefit__title b{display:block;color:var(--ink);font-weight:700}
.benefit p{font-size:4.6px;line-height:1.45;color:var(--muted)}
.contact-band{left:180px;top:532px;width:240px;height:62px}
.contact{left:202px;top:548px;color:var(--white)}
.contact__call{font-family:"Montserrat",sans-serif;font-size:10px;font-weight:500;letter-spacing:.4px}
.contact__call span{font-size:12px;font-weight:600}
.contact__line{display:flex;align-items:center;gap:4px;font-size:5.6px;margin-top:2px}
.contact__line i{width:5px;height:5px;border-radius:50%;background:var(--white);display:inline-block}
.stripes{left:0;top:573px;width:180px;height:21px}

/* back */
.server-photo{left:0;top:0;width:420px;height:230px;background:linear-gradient(90deg,#8aa0b6 0%,#dfe7ee 30%,#f4f7fa 50%,#dfe7ee 70%,#8aa0b6 100%)}
.back-band{left:0;top:200px;width:420px;height:60px}
.select{left:0;top:222px;width:420px;text-align:center}
.select .heading{font-size:12px}
.select p{font-size:5.6px;line-height:1.45;color:var(--muted);width:330px;margin:8px auto 0}
.plans{left:24px;top:278px;display:flex;gap:12px}
.plan{width:116px;height:166px;background:#f0f1f3;border-radius:3px;padding:10px 8px 0;text-align:center;position:relative}
.plan__head{display:flex;align-items:center;justify-content:center;gap:5px;font-family:"Montserrat",sans-serif;font-size:6.6px;font-weight:700;line-height:1.15;height:20px}
.plan__head svg{width:15px;height:15px}
.plan__rule{height:1px;background:var(--line);margin:6px 0}
.price{color:var(--blue);font-family:"Montserrat",sans-serif;display:flex;align-items:flex-start;justify-content:center;gap:2px}
.price small{font-size:5.5px;color:var(--ink);align-self:center;margin-top:6px}
.price sup{font-size:8px;margin-top:2px}
.price strong{font-size:21px;font-weight:600;line-height:1}
.price-unit{font-size:5.5px;color:var(--blue);margin-bottom:6px}
.plan ul{list-style:none;font-size:4.6px;color:var(--muted)}
.plan li{padding:3px 0;border-bottom:1px solid #e0e3e7}
.plan__btn{position:absolute;left:14px;right:14px;bottom:10px;height:13px;border-radius:7px;background:var(--ink);color:var(--white);font-family:"Montserrat",sans-serif;font-size:5px;font-weight:700;display:flex;align-items:center;justify-content:center;letter-spacing:.4px}
.reviews{left:0;top:462px;width:420px;text-align:center}
.reviews .heading{font-size:11px}
.reviews__rule{width:26px;height:1px;background:var(--muted);margin:4px auto 10px}
.review-row{display:flex;justify-content:space-between;padding:0 30px}
.review{width:78px}
.review svg{width:16px;height:16px}
.review__who{font-family:"Montserrat",sans-serif;font-size:5.6px;font-weight:700;color:var(--blue);margin:3px 0 2px}
.review p{font-size:4.5px;line-height:1.4;color:var(--muted)}
.footer{left:0;top:574px;width:420px;height:20px;background:var(--blue);color:var(--white);display:flex;justify-content:space-around;align-items:center;font-size:5.6px}
.footer span{display:flex;align-items:center;gap:4px}
.footer i{width:5px;height:5px;border-radius:50%;background:var(--white);display:inline-block}
</style>
</head>
<body>

<section class="page page--front">
  <div class="abs hero-photo" role="img" aria-label="Photo of two colleagues working together at a table with a laptop and documents"></div>
  <div class="abs brand"><span class="brand__mark"></span><span class="brand__name">BRENVARO</span></div>
  <h1 class="abs hero-title">JUST<br>WORK</h1>
  <p class="abs hero-sub">We Offer Small Companies The<br>Workplace Of The Future!<br>Safe, Fast And Innovative. Work<br>From Anywhere!</p>
  <svg class="abs band" viewBox="0 0 420 60" preserveAspectRatio="none">
    <polygon points="0,26 170,40 420,12 420,22 170,50 0,36" fill="#1f6fc5"/>
    <polygon points="0,36 170,50 420,22 420,60 0,60" fill="#ffffff"/>
    <polygon points="0,36 170,50 170,60 0,60" fill="#ececec"/>
  </svg>

  <div class="abs about">
    <h2 class="heading">ABOUT US</h2>
    <div class="about__rule"></div>
    <div class="about__label">THE FOUNDERS</div>
    <p>The company Brenvaro was founded on March 18th, 2019 by Jonas Feldtner and Lukas Ohrmann. The foundation was preceded by a two-year test and project planning phase. The company's headquarters are located on the tranquil Lake Ardsee.</p>
    <div class="founder">
      <div class="founder__photo" role="img" aria-label="Portrait photo of founder Lukas Ohrmann"></div>
      <div>
        <div class="founder__name">Lukas Ohrmann</div>
        <div class="founder__role">Founder and CEO</div>
        <p>Lukas is 46 years old, married and has two children. He has been working in IT for 19 years now and has started as a trained businessman.</p>
      </div>
    </div>
    <div class="founder">
      <div class="founder__photo" role="img" aria-label="Portrait photo of founder Jonas Feldtner"></div>
      <div>
        <div class="founder__name">Jonas Feldtner</div>
        <div class="founder__role">Founder and CEO</div>
        <p>Jonas is 34 years old and single. Since training as a IT specialist and studying IT, he has been working in the IT industry for over 15 years.</p>
      </div>
    </div>
  </div>

  <div class="abs benefits">
    <h2 class="heading">YOUR BENEFITS</h2>
    <div class="benefits__rule"></div>
    <div class="benefit-grid">
      <div class="benefit">
        <div class="benefit__head"><svg viewBox="0 0 14 14"><circle cx="7" cy="8" r="5" fill="none" stroke="#1f6fc5" stroke-width="1.6"/><path d="M7 8V5.5M5.5 1.5h3" stroke="#1f6fc5" stroke-width="1.4"/></svg><div class="benefit__title">Express<b>Suppression</b></div></div>
        <p>From Monday to Friday, the troubleshooting is carried out in a maximum of 8 hours by our simple support.</p>
      </div>
      <div class="benefit">
        <div class="benefit__head"><svg viewBox="0 0 14 14"><path d="M7 1c2.5 2 3 5 2 8H5C4 6 4.5 3 7 1z" fill="#1f6fc5"/><path d="M5 9l-2 3M9 9l2 3" stroke="#1f6fc5" stroke-width="1.2"/></svg><div class="benefit__title">Fast<b>Programs</b></div></div>
        <p>Our technology gets the maximum speed out of your existing applications.</p>
      </div>
      <div class="benefit">
        <div class="benefit__head"><svg viewBox="0 0 14 14"><path d="M7 1l5 2v4c0 3-2.5 5-5 6-2.5-1-5-3-5-6V3z" fill="#1f6fc5"/><path d="M4.8 7l1.6 1.6L9.4 5.6" stroke="#fff" stroke-width="1.2" fill="none"/></svg><div class="benefit__title">Professional<b>Protection</b></div></div>
        <p>Our service includes professional protection against viruses, crypto viruses, trojans and other pests.</p>
      </div>
      <div class="benefit">
        <div class="benefit__head"><svg viewBox="0 0 14 14"><rect x="2" y="2" width="10" height="3" rx="1" fill="#1f6fc5"/><rect x="2" y="6" width="10" height="3" rx="1" fill="#1f6fc5"/><rect x="2" y="10" width="10" height="3" rx="1" fill="#1f6fc5"/></svg><div class="benefit__title">Data<b>Backup</b></div></div>
        <p>Daily data backup and thus protection against data loss - controlled by us and can be restored at any time.</p>
      </div>
      <div class="benefit">
        <div class="benefit__head"><svg viewBox="0 0 14 14"><circle cx="7" cy="5" r="3.5" fill="#1f6fc5"/><path d="M2 13c0-3 2-4.5 5-4.5s5 1.5 5 4.5z" fill="#1f6fc5"/></svg><div class="benefit__title">Predictable<b>Costs</b></div></div>
        <p>Linear monthly cost distribution. There are no additional costs due to defects, extensions or expensive on-site operations.</p>
      </div>
      <div class="benefit">
        <div class="benefit__head"><svg viewBox="0 0 14 14"><rect x="1" y="2" width="12" height="8" rx="1" fill="none" stroke="#1f6fc5" stroke-width="1.4"/><rect x="5" y="11" width="4" height="2" fill="#1f6fc5"/><circle cx="7" cy="6" r="2" fill="#1f6fc5"/></svg><div class="benefit__title">High<b>Security</b></div></div>
        <p>Central IT services from highly secure data centres.</p>
      </div>
    </div>
  </div>

  <svg class="abs contact-band" viewBox="0 0 240 62" preserveAspectRatio="none">
    <polygon points="10,8 240,0 240,62 0,62" fill="#1f6fc5"/>
  </svg>
  <div class="abs contact">
    <div class="contact__call">CALL US NOW: <span>0123 987650</span></div>
    <div class="contact__line"><i></i>www.beta.brenvaro.de</div>
    <div class="contact__line"><i></i>betabrenvaro@mailpost.de</div>
  </div>
  <svg class="abs stripes" viewBox="0 0 180 21">
    <rect x="0" y="0" width="180" height="3" fill="#222831"/>
    <g fill="#1f6fc5">
      <polygon points="6,21 12,7 16,7 10,21"/><polygon points="18,21 24,7 28,7 22,21"/><polygon points="30,21 36,7 40,7 34,21"/><polygon points="42,21 48,7 52,7 46,21"/><polygon points="54,21 60,7 64,7 58,21"/><polygon points="66,21 72,7 76,7 70,21"/>
    </g>
  </svg>
</section>

<section class="page page--back">
  <div class="abs server-photo" role="img" aria-label="Photo of a man in a shirt and tie standing in a bright server room aisle"></div>
  <svg class="abs back-band" viewBox="0 0 420 60" preserveAspectRatio="none">
    <path d="M0,16 Q210,-4 420,16 L420,60 L0,60 Z" fill="#1f6fc5"/>
    <path d="M0,22 Q210,4 420,22 L420,60 L0,60 Z" fill="#ffffff"/>
  </svg>
  <div class="abs select">
    <h2 class="heading">SELECT SERVICE</h2>
    <p>Choose your service. Brenvaro provides a complete workstation in the thin client model. All you need is a monitor to start working. Both services can be used encrypted from any location with an existing PC, laptop or tablet.</p>
  </div>

  <div class="abs plans">
    <div class="plan">
      <div class="plan__head"><svg viewBox="0 0 14 14"><circle cx="7" cy="4" r="3" fill="#1f6fc5"/><path d="M2 13c0-4 2-6 5-6s5 2 5 6z" fill="#1f6fc5"/></svg>THIN CLIENT</div>
      <div class="plan__rule"></div>
      <div class="price"><small>from</small><sup>€</sup><strong>89</strong></div>
      <div class="price-unit">per user / month</div>
      <ul><li>Minimum term is 12 months</li><li>Thin client per user included</li><li>Licensing of the Norvik operating system</li><li>Max. 8 hours reaction time</li></ul>
      <div class="plan__btn">GET STARTED NOW</div>
    </div>
    <div class="plan">
      <div class="plan__head"><svg viewBox="0 0 14 14"><rect x="1" y="2" width="12" height="8" rx="1" fill="none" stroke="#1f6fc5" stroke-width="1.4"/><rect x="4" y="11.5" width="6" height="1.5" fill="#1f6fc5"/></svg>MOBILE THIN<br>CLIENT</div>
      <div class="plan__rule"></div>
      <div class="price"><small>from</small><sup>€</sup><strong>99</strong></div>
      <div class="price-unit">per user / month</div>
      <ul><li>Minimum term is 12 months</li><li>Support and management</li><li>Licensing of the Norvik operating system</li><li>Max. 8 hours reaction time</li></ul>
      <div class="plan__btn">GET STARTED NOW</div>
    </div>
    <div class="plan">
      <div class="plan__head"><svg viewBox="0 0 14 14"><circle cx="7" cy="6" r="3" fill="#1f6fc5"/><rect x="5.5" y="10" width="3" height="2.5" fill="#1f6fc5"/><path d="M7 0.5v1.5M1.5 6H3M11 6h1.5M2.8 2l1 1M11.2 2l-1 1" stroke="#1f6fc5" stroke-width="1"/></svg>BRING YOUR<br>OWN</div>
      <div class="plan__rule"></div>
      <div class="price"><small>from</small><sup>€</sup><strong>75</strong></div>
      <div class="price-unit">per user / month</div>
      <ul><li>No minimum term</li><li>Use with your own device</li><li>Licensing of the Norvik operating system</li><li>Max. 8 hours reaction time</li></ul>
      <div class="plan__btn">GET STARTED NOW</div>
    </div>
  </div>

  <div class="abs reviews">
    <h2 class="heading">WHAT OUR CUSTOMERS SAY</h2>
    <div class="reviews__rule"></div>
    <div class="review-row">
      <div class="review">
        <svg viewBox="0 0 16 16"><path d="M2 8L8 3l6 5v6H2z" fill="none" stroke="#555" stroke-width="1.4"/><rect x="6.5" y="10" width="3" height="4" fill="#555"/></svg>
        <div class="review__who">Hausverwalter</div>
        <p>I can work anywhere. Competition had to fix for beneficiaries after a cryptovirus. My data is safe.</p>
      </div>
      <div class="review">
        <svg viewBox="0 0 16 16"><circle cx="8" cy="5" r="3" fill="#555"/><path d="M3 15c0-4 2-6 5-6s5 2 5 6z" fill="#555"/></svg>
        <div class="review__who">Electrician</div>
        <p>We have grown in recent years. With Brenvaro we have found a solution that scales without one-off costs.</p>
      </div>
      <div class="review">
        <svg viewBox="0 0 16 16"><circle cx="6" cy="6" r="3" fill="#555"/><path d="M1 15c0-4 2-5.5 5-5.5s5 1.5 5 5.5z" fill="#555"/><rect x="10" y="1" width="5" height="4" rx="1" fill="#555"/></svg>
        <div class="review__who">Quality consultant</div>
        <p>I started my company recently. The monthly payment of the services offers great financial flexibility.</p>
      </div>
      <div class="review">
        <svg viewBox="0 0 16 16"><path d="M2 6l1-4h10l1 4z" fill="#555"/><rect x="3" y="7" width="10" height="7" fill="none" stroke="#555" stroke-width="1.4"/><rect x="6.5" y="10" width="3" height="4" fill="#555"/></svg>
        <div class="review__who">Retailer</div>
        <p>For us, Brenvaro solved significant speed issues in our software. We are happy now!</p>
      </div>
    </div>
  </div>

  <div class="abs footer">
    <span><i></i>www.beta.brenvaro.de</span>
    <span><i></i>betabrenvaro@mailpost.de</span>
  </div>
</section>

</body>
</html>
```